Cedar Row Maintenance and Concierge Flyer

We need a flyer for cedar row maintenance and concierge service. We specialize in and provide residential maintenance and errand services to retired and semi retired persons living in the Lake Norman area. The services we include:
Lighting and plumbing repairs
Ceiling fan installation
Handicap accessories
Locks and security
Picture hanging
Hang blinds
Furniture arrangement / assembly
Pressure washing
Battery Jump start
and more...

Our Concierge services include:
Errand running
Grocery shopping
Wellness Checks
Dog Walk
Garbage Collection
and more...

We offer monthly service agreements and 24/7 access
Call text or e-mail for more information
704.555.0187
1cedarrowmaint@quillpostmail.com

The design should invoke a sense of trust and a customer service driven mission

Target Market(s)

Residential maintenance

Industry/Entity Type

Property Maintenance

Contact Information for Business Card

Derek Halvorsen
48176 Quimby Ferrel Rd.
Cornelius NC 28031
704.555.0187
with uploaded logo

Requirements
Nice to have
• Would like a postcard size flyer. Front and back
Should not have
• No pics of of people wearing hard hats or pics of blueprints. No pics of commercial or industrial maintenance.

```html
<!DOCTYPE html>
<html lang="en">
<head>
<meta charset="utf-8">
<title>Cedar Row Maintenance and Concierge – Flyer Front and Back</title>
<link href="https://fonts.googleapis.com/css2?family=Montserrat:wght@400;500;600;700&display=swap" rel="stylesheet">
<style>
  :root{
    --stage:#4a4f4f;
    --paper:#ffffff;
    --ink:#2b2d33;
    --slate:#33363f;
    --red:#cf2027;
    --grey-band:#d7d8da;
    --logo-grey:#6b6b6d;
    --text-dark:#2e3034;
  }
  *{box-sizing:border-box;margin:0;padding:0}
  html,body{width:1200px;height:936px;overflow:hidden}
  body{background:var(--stage);font-family:"Montserrat",Arial,sans-serif;position:relative}

  .flyer{position:absolute;top:77px;width:506px;height:781px;background:var(--paper);box-shadow:0 4px 14px rgba(0,0,0,.35);overflow:hidden}
  .flyer--front{left:71px}
  .flyer--back{left:635px}

  .masthead{position:absolute;left:0;top:0;width:100%;height:130px;display:flex;align-items:center;justify-content:center;gap:14px}
  .masthead__dot{width:44px;height:44px;border-radius:50%;background:var(--red);flex:none}
  .masthead__name{font-weight:500;font-size:19px;line-height:1.25;color:var(--logo-grey);text-transform:uppercase;letter-spacing:.5px}

  .photo{position:absolute;left:0;width:100%}
  .photo--front{top:130px;height:331px;background:linear-gradient(120deg,#6f7c6a 0%,#c9cccf 35%,#e6e7e9 60%,#9b3a3a 100%)}
  .photo--back{top:345px;height:353px;background:linear-gradient(100deg,#6d5a4f 0%,#4f5864 35%,#3b4454 65%,#6a5e63 100%)}

  .intro{position:absolute;left:0;top:461px;width:359px;height:237px;background:var(--slate);color:#fff;padding:38px 0 0 40px}
  .intro__lead{font-size:16px;font-weight:500}
  .intro__title{font-size:25px;font-weight:700;line-height:33px;margin:6px 0 4px;letter-spacing:.3px}
  .intro__sub{font-size:15px;line-height:19px;font-weight:500}

  .offer{position:absolute;left:359px;top:461px;width:147px;height:237px;background:var(--red);color:#fff;padding:47px 0 0 15px}
  .offer__text{font-size:14px;font-weight:500;line-height:17px}
  .offer__icon{display:block;margin:12px 0 4px}
  .offer__big{font-size:23px;font-weight:700;line-height:26px}
  .offer__small{font-size:14px;font-weight:700;letter-spacing:.5px}

  .contact{position:absolute;left:0;top:698px;width:100%;height:83px;text-align:center;padding-top:20px}
  .contact__call{color:var(--red);font-size:13px;font-weight:500}
  .contact__row{display:flex;justify-content:center;align-items:center;gap:16px;margin-top:8px;font-size:15.5px;color:var(--text-dark)}
  .contact__phone{font-weight:700;display:flex;align-items:center;gap:6px}
  .contact__mail{font-weight:500;display:flex;align-items:center;gap:6px}

  .services{position:absolute;left:0;top:130px;width:100%;height:215px;background:var(--grey-band);padding:28px 0 0 60px;color:var(--text-dark)}
  .services__title{color:var(--red);font-size:14.5px;font-weight:600;margin-bottom:8px}
  .services__cols{display:flex;gap:14px}
  .services__list{list-style:none;font-size:14.5px;line-height:23px;font-weight:500}
  .services__list li{position:relative;padding-left:12px}
  .services__list li::before{content:"•";position:absolute;left:0}
  .services__list .wrap{display:block;line-height:19px;margin-bottom:4px}
  .services__list .more{padding-left:12px;font-size:11.5px}
  .services__list .more::before{content:none}
  .services__list--a{width:184px}

  .concierge{position:absolute;left:35px;top:524px;color:#fff}
  .concierge__title{font-size:12.5px;font-weight:500}
  .concierge__title b{font-size:14.5px;font-weight:700}
  .concierge__list{list-style:none;margin-top:5px;font-size:14.5px;font-weight:700;line-height:20.5px}
  .concierge__list li::before{content:"•";color:var(--red);margin-right:6px}
  .concierge__more{font-size:11.5px;font-weight:500;margin-top:2px}
</style>
</head>
<body>

<section class="flyer flyer--front">
  <header class="masthead">
    <span class="masthead__dot"></span>
    <span class="masthead__name">Cedar Row<br>Maintenance &amp; Concierge</span>
  </header>
  <div class="photo photo--front" role="img" aria-label="Photo of a friendly handyman on a stepladder holding a ceiling light, chatting with a smiling older woman at home, red toolbox beside him"></div>
  <div class="intro">
    <p class="intro__lead">We Provide you</p>
    <h1 class="intro__title">RESIDENTIAL<br>MAINTENANCE &amp;<br>ERRAND SERVICES</h1>
    <p class="intro__sub">to retired and semi retired persons<br>living in the Lake Norman area.</p>
  </div>
  <div class="offer">
    <p class="offer__text">We offer<br>monthly service<br>agreements &amp;</p>
    <svg class="offer__icon" width="44" height="34" viewBox="0 0 44 34" aria-hidden="true">
      <circle cx="22" cy="17" r="14" fill="none" stroke="#fff" stroke-width="2.4"/>
      <path d="M4 6c-2 2-2 5 0 8l5 6c2 2 4 2 6 1l-3-5-2 1-3-4 1-2-4-5z" fill="#fff"/>
      <text x="22" y="22" text-anchor="middle" font-family="Montserrat,Arial,sans-serif" font-weight="700" font-size="13" fill="#fff">24</text>
    </svg>
    <p class="offer__big">24/7</p>
    <p class="offer__small">ACCESS</p>
  </div>
  <footer class="contact">
    <p class="contact__call">Call text or e-mail for more information</p>
    <div class="contact__row">
      <span class="contact__phone"><svg width="13" height="13" viewBox="0 0 24 24" aria-hidden="true"><path fill="#cf2027" d="M6.6 10.8a15 15 0 006.6 6.6l2.2-2.2c.3-.3.7-.4 1-.2 1.1.4 2.3.6 3.6.6.6 0 1 .4 1 1V20c0 .6-.4 1-1 1A17 17 0 013 4c0-.6.4-1 1-1h3.5c.6 0 1 .4 1 1 0 1.3.2 2.5.6 3.6.1.3 0 .7-.2 1z"/></svg>704.555.0187</span>
      <span class="contact__mail"><svg width="14" height="11" viewBox="0 0 14 11" aria-hidden="true"><rect x="0.7" y="0.7" width="12.6" height="9.6" fill="none" stroke="#cf2027" stroke-width="1.3"/><path d="M1 1l6 5 6-5" fill="none" stroke="#cf2027" stroke-width="1.3"/></svg>1cedarrowmaint@quillpostmail.com</span>
    </div>
  </footer>
</section>

<section class="flyer flyer--back">
  <header class="masthead">
    <span class="masthead__dot"></span>
    <span class="masthead__name">Cedar Row<br>Maintenance &amp; Concierge</span>
  </header>
  <div class="services">
    <h2 class="services__title">The services we include:</h2>
    <div class="services__cols">
      <ul class="services__list services__list--a">
        <li class="wrap">Lighting and<br>plumbing repairs</li>
        <li>Ceiling fan installation</li>
        <li>Handicap accessories</li>
        <li>Locks and security</li>
        <li>Picture hanging</li>
      </ul>
      <ul class="services__list">
        <li>Hang blinds</li>
        <li class="wrap">Furniture arrangement<br>/assembly</li>
        <li>Pressure washing</li>
        <li>Battery Jump start</li>
        <li class="more">and more...</li>
      </ul>
    </div>
  </div>
  <div class="photo photo--back" role="img" aria-label="Photo of a helper carrying a woven grocery basket up to a front door where an older woman waits, softly blurred"></div>
  <div class="concierge">
    <p class="concierge__title">Our <b>CONCIERGE SERVICES</b> include:</p>
    <ul class="concierge__list">
      <li>Errand running</li>
      <li>Grocery shopping</li>
      <li>Wellness Checks</li>
      <li>Dog Walk</li>
      <li>Garbage Collection</li>
    </ul>
    <p class="concierge__more">and more...</p>
  </div>
  <footer class="contact">
    <p class="contact__call">Call text or e-mail for more information</p>
    <div class="contact__row">
      <span class="contact__phone"><svg width="13" height="13" viewBox="0 0 24 24" aria-hidden="true"><path fill="#cf2027" d="M6.6 10.8a15 15 0 006.6 6.6l2.2-2.2c.3-.3.7-.4 1-.2 1.1.4 2.3.6 3.6.6.6 0 1 .4 1 1V20c0 .6-.4 1-1 1A17 17 0 013 4c0-.6.4-1 1-1h3.5c.6 0 1 .4 1 1 0 1.3.2 2.5.6 3.6.1.3 0 .7-.2 1z"/></svg>704.555.0187</span>
      <span class="contact__mail"><svg width="14" height="11" viewBox="0 0 14 11" aria-hidden="true"><rect x="0.7" y="0.7" width="12.6" height="9.6" fill="none" stroke="#cf2027" stroke-width="1.3"/><path d="M1 1l6 5 6-5" fill="none" stroke="#cf2027" stroke-width="1.3"/></svg>1cedarrowmaint@quillpostmail.com</span>
    </div>
  </footer>
</section>

</body>
</html>
```